Veltrano - Mechanic/Collision Center Business Card

We're looking for a business card design for our mechanic/ collision repair shop.

Can be with colours or monochromatic.

See the attached files.

Many thanks

```html
<!DOCTYPE html>
<html lang="en">
<head>
<meta charset="utf-8">
<title>Veltrano Business Card</title>
<link href="https://fonts.googleapis.com/css2?family=Roboto:wght@400;500;700;900&display=swap" rel="stylesheet">
<style>
  :root {
    --page: #3a3a3c;
    --card-dark: #111213;
    --card-dark-mid: #1e1f21;
    --brand-blue: #1ea0dc;
    --tool-grey: #6f7073;
    --text-light: #ffffff;
    --text-soft: #e6f4fb;
  }
  * { margin: 0; padding: 0; box-sizing: border-box; }
  html, body {
    width: 1200px; height: 960px; overflow: hidden;
    background: var(--page);
    font-family: "Roboto", Arial, sans-serif;
  }
  .canvas { position: relative; width: 1200px; height: 960px; }
  .card {
    position: absolute; width: 620px; height: 354px; overflow: hidden;
    box-shadow: 0 14px 30px rgba(0,0,0,.45);
  }
  .card-back {
    left: 90px; top: 90px;
    background: radial-gradient(ellipse at 50% 40%, var(--card-dark-mid), var(--card-dark) 70%);
  }
  .card-front {
    left: 490px; top: 510px;
    background: radial-gradient(ellipse at 75% 40%, var(--card-dark-mid), var(--card-dark) 70%);
  }
  .wordmark {
    display: flex; align-items: center; gap: 14px;
    color: var(--text-light); font-weight: 900; letter-spacing: 1px;
  }
  .wordmark-dot { border-radius: 50%; background: var(--brand-blue); flex: none; }
  .card-back .wordmark {
    position: absolute; left: 0; right: 0; top: 120px; justify-content: center; font-size: 52px;
  }
  .card-back .wordmark-dot { width: 40px; height: 40px; }
  .back-url {
    position: absolute; left: 0; right: 0; top: 236px; text-align: center;
    color: var(--text-light); font-size: 15px; letter-spacing: 6px; font-weight: 400;
  }
  .front-panel {
    position: absolute; left: 0; top: 0; bottom: 0; width: 300px;
    background: var(--brand-blue);
  }
  .tool-band { position: absolute; left: 270px; top: 0; width: 90px; height: 354px; }
  .card-front .wordmark {
    position: absolute; left: 380px; top: 150px; font-size: 36px; gap: 10px;
  }
  .card-front .wordmark-dot { width: 26px; height: 26px; }
  .contact { position: absolute; left: 38px; top: 92px; color: var(--text-light); }
  .contact-name { font-size: 22px; font-weight: 500; letter-spacing: .5px; }
  .contact-role { font-size: 15px; margin-bottom: 16px; color: var(--text-soft); }
  .contact-address { font-size: 14px; line-height: 1.35; margin-bottom: 12px; }
  .contact-list { list-style: none; font-size: 14px; line-height: 1.5; }
  .contact-list li { display: flex; align-items: center; gap: 9px; }
  .contact-list svg { width: 13px; height: 13px; flex: none; fill: var(--text-light); }
</style>
</head>
<body>
<div class="canvas">

  <section class="card card-back">
    <div class="wordmark"><span class="wordmark-dot"></span>VELTRANO</div>
    <div class="back-url">WWW.VELTRANO.COM</div>
  </section>

  <section class="card card-front">
    <div class="front-panel"></div>
    <svg class="tool-band" viewBox="0 0 90 354" role="img" aria-label="Large grey wrench illustration">
      <path d="M0 0 H90 V354 H30 Z" fill="var(--tool-grey)"/>
    </svg>

    <div class="contact">
      <div class="contact-name">DANIEL HARKER</div>
      <div class="contact-role">President</div>
      <div class="contact-address">4120 Birchwood Road<br>Fairbanks, Alaska 99701</div>
      <ul class="contact-list">
        <li><svg viewBox="0 0 16 16"><path d="M3 1l3 3-1.5 2a9 9 0 005 5L11.5 9.5l3 3L12.5 15C6 14 2 10 1 3.5z"/></svg>555-210-4471</li>
        <li><svg viewBox="0 0 16 16"><path d="M4 0h8a1 1 0 011 1v14a1 1 0 01-1 1H4a1 1 0 01-1-1V1a1 1 0 011-1zm1 2v10h6V2z"/></svg>555-318-2096</li>
        <li><svg viewBox="0 0 16 16"><path d="M4 1h8v4H4zM1 6h14v7h-3v2H4v-2H1zm4 5v3h6v-3z"/></svg>555-406-7732</li>
        <li><svg viewBox="0 0 16 16"><path d="M1 3h14v10H1zm1.5 1.5L8 9l5.5-4.5z"/></svg>info@veltrano.com</li>
        <li><svg viewBox="0 0 16 16"><circle cx="8" cy="8" r="7"/></svg>www.veltrano.com</li>
      </ul>
    </div>

    <div class="wordmark"><span class="wordmark-dot"></span>VELTRANO</div>
  </section>

</div>
</body>
</html>
```